New Webpage for High Class Expert Witness Services Company

We are looking for a minimalist design for a webpage that just has our logo and an entry form offer to connect with one of our Liaisons.
The entry form should just ask for Name, Email, Contact Info and Description of Project.

Company Name is: The Marlow Crest Advisory Services

Number of Pages Required

1 page

```html
<!DOCTYPE html>
<html lang="en">
<head>
<meta charset="UTF-8">
<title>The Marlow Crest Advisory Services — Connect with a Liaison</title>
<link rel="stylesheet" href="https://fonts.googleapis.com/css2?family=Marcellus&family=Hanken+Grotesk:wght@400;500&display=swap">
<style>
  :root {
    --ink: #111112;
    --panel: #121213;
    --paper: #ffffff;
    --text-light: #f4f4f4;
    --muted-light: #b9b9b9;
    --label: #9a9a9a;
    --rule: #bdbdbd;
    --brand-silver: #d9d9d9;
  }
  * { box-sizing: border-box; margin: 0; padding: 0; }
  html, body { width: 1200px; height: 732px; overflow: hidden; background: var(--paper); }
  body { font-family: "Hanken Grotesk", Arial, sans-serif; position: relative; }

  .intro {
    position: absolute; left: 0; top: 0; width: 598px; height: 732px;
    background: var(--panel); color: var(--text-light);
  }
  .brand {
    position: absolute; left: 78px; top: 150px;
    display: flex; align-items: center; gap: 14px;
  }
  .brand-mark { width: 30px; height: 30px; background: var(--brand-silver); }
  .brand-name {
    font-family: "Marcellus", Georgia, serif; font-size: 27px;
    letter-spacing: 1px; color: var(--brand-silver); white-space: nowrap;
  }
  .intro-title {
    position: absolute; left: 78px; top: 228px;
    font-family: "Marcellus", Georgia, serif; font-weight: 400;
    font-size: 44px; line-height: 48px; color: var(--text-light);
  }
  .intro-text {
    position: absolute; left: 78px; top: 332px; width: 440px;
    font-size: 17px; line-height: 24px;
  }
  .copyright {
    position: absolute; left: 78px; top: 686px;
    font-size: 11.5px; color: var(--muted-light);
  }

  .contact { position: absolute; left: 662px; top: 0; width: 472px; }
  .contact-title {
    position: absolute; top: 118px; left: 0;
    font-family: "Marcellus", Georgia, serif; font-weight: 400;
    font-size: 50px; line-height: 60px; color: var(--ink);
  }
  .field {
    position: absolute; left: 0; width: 472px;
    border-bottom: 1px solid var(--rule); padding-left: 28px;
  }
  .field-label { display: block; font-size: 11.5px; color: var(--label); line-height: 14px; }
  .field-value { display: block; font-size: 14.5px; color: var(--ink); margin-top: 10px; line-height: 18px; }
  .f-name { top: 204px; height: 53px; }
  .f-email { top: 286px; height: 53px; }
  .f-phone { top: 372px; height: 52px; }
  .f-project { top: 455px; height: 52px; }

  .send {
    position: absolute; left: 0; top: 542px; width: 472px; height: 58px;
    border-radius: 29px; background: var(--ink); color: var(--paper);
    border: none; font-family: inherit; font-size: 15px; font-weight: 500;
    letter-spacing: .3px;
  }
</style>
</head>
<body>
  <section class="intro">
    <div class="brand">
      <span class="brand-mark"></span>
      <span class="brand-name">THE MARLOW CREST</span>
    </div>
    <h1 class="intro-title">The Marlow Crest<br>Advisory Services</h1>
    <p class="intro-text">Suspendisse ipsum augue, feugiat consectetur mauris a, varius commodo ante. Aenean venenatis ultricies sapien, quis luctus quam ultricies eget.</p>
    <p class="copyright">© Copyright 2026 | The Marlow Crest Advisory Services | All Right Reserved</p>
  </section>

  <form class="contact">
    <h2 class="contact-title">Welcome!</h2>
    <div class="field f-name"><span class="field-label">Name</span><span class="field-value">Evan Parrish</span></div>
    <div class="field f-email"><span class="field-label">Email</span><span class="field-value">abc@mailbox.com</span></div>
    <div class="field f-phone"><span class="field-label">Phone Number</span><span class="field-value">123-456-7890</span></div>
    <div class="field f-project"><span class="field-label">Project Discription</span><span class="field-value">type here...</span></div>
    <button class="send" type="button">SEND</button>
  </form>
</body>
</html>
```